Business Card Design Project used as hotel key

I need a project to be printed on PVC card and used by our customers as room key.

The design and the color are up to you. My idea would be to include the logo (colour can also be changed) on the front side and our Internet address on the back (http://www.valmirenza.ch, info@valmirenza.ch).

Target Market(s)

Hôtel customers

Industry/Entity Type

Hotel

Requirements
Must have
• I have attached below the template of the front and back of the card. The logo on the back shown on the template below the magnetic stripe should not be used.

Must have:

1. Follow the template size (shown in the template):

Full Bleed Size:
3.55" x 2.3"
90.17mm x 58.42mm
1065 x 690 pixels

Trim Size:
3.375" x 2.125"
85.77mm x 54.02mm
1013 x 638 pixels

A bleed is the outer area of your artwork that falls on the outside of the trim line. It is important that you do not have any important information in the bleed area as ¼ “ will be cut off on all sides. Cards with a “framed border” are not recommended due to variances in die cutting.

2. Make sure you leave the area between the magstripe markers on the template blank.

3. There need to be an arrow on the front side (on the left), pointing the left side

4. Color: Full color both sides, color process CMYK. 300 DPI at 100% of the final print size

```html
<!DOCTYPE html>
<html lang="en">
<head>
<meta charset="utf-8">
<title>Hôtel Valmirenza – Room Key Card</title>
<link rel="stylesheet" href="https://fonts.googleapis.com/css2?family=Questrial&display=swap">
<style>
  :root {
    --mint: #b2eedd;
    --leaf: #b4f29a;
    --ink: #3a3638;
    --arrow-dark: #4a4045;
    --white: #ffffff;
    --rule: #1a1a1a;
  }
  * { margin: 0; padding: 0; box-sizing: border-box; }
  html, body { width: 926px; height: 1200px; overflow: hidden; background: var(--mint); }
  .card-sheet {
    position: relative;
    width: 926px;
    height: 1200px;
    font-family: "Questrial", sans-serif;
    color: var(--ink);
  }
  .card-side {
    position: absolute;
    left: 0;
    width: 926px;
    height: 600px;
    overflow: hidden;
  }
  .card-front { top: 0; }
  .card-back { top: 601px; height: 599px; }
  .tree-backdrop {
    position: absolute;
    inset: 0;
    background:
      radial-gradient(ellipse at 25% 55%, rgba(180,242,154,0.55), transparent 60%),
      radial-gradient(ellipse at 68% 45%, rgba(180,242,154,0.6), transparent 55%),
      linear-gradient(160deg, var(--mint), #b6f0c6 55%, var(--mint));
  }
  .side-divider {
    position: absolute;
    left: 0;
    top: 599px;
    width: 926px;
    height: 2px;
    background: var(--rule);
  }
  .front-arrow {
    position: absolute;
    left: 0;
    top: 0;
    width: 926px;
    height: 600px;
  }
  .brand-mark {
    position: absolute;
    left: 290px;
    top: 200px;
    width: 520px;
    text-align: center;
    color: var(--white);
    font-weight: 400;
    line-height: 1;
    white-space: nowrap;
  }
  .brand-mark .brand-small { display: block; font-size: 38px; letter-spacing: 3px; }
  .brand-mark .brand-large { display: block; font-size: 74px; letter-spacing: 1px; margin-top: 14px; }
  .room-key-label {
    position: absolute;
    left: 290px;
    width: 520px;
    top: 452px;
    text-align: center;
    font-size: 47px;
    color: var(--ink);
  }
  .back-brand {
    position: absolute;
    left: 370px;
    top: 382px;
    width: 200px;
    text-align: center;
    color: var(--white);
    line-height: 1;
    white-space: nowrap;
  }
  .back-brand .brand-small { display: block; font-size: 13px; letter-spacing: 1px; }
  .back-brand .brand-large { display: block; font-size: 26px; margin-top: 4px; }
  .contact-line {
    position: absolute;
    top: 474px;
    font-size: 30px;
    color: var(--ink);
    white-space: nowrap;
  }
  .contact-web { left: 113px; }
  .contact-mail { left: 523px; }
</style>
</head>
<body>
  <main class="card-sheet">
    <section class="card-side card-front">
      <div class="tree-backdrop" role="img" aria-label="Bare winter trees silhouetted in light green on a mint background"></div>
      <svg class="front-arrow" viewBox="0 0 926 600" aria-hidden="true">
        <defs>
          <linearGradient id="arrow-fade" x1="60" y1="0" x2="255" y2="0" gradientUnits="userSpaceOnUse">
            <stop offset="0" stop-color="#4a4045"/>
            <stop offset="0.45" stop-color="#4a4045" stop-opacity="0.85"/>
            <stop offset="1" stop-color="#b2eedd" stop-opacity="0"/>
          </linearGradient>
        </defs>
        <polygon class="arrow-shape" points="255,113 60,296 255,483 168,296" fill="url(#arrow-fade)"/>
      </svg>
      <div class="brand-mark">
        <span class="brand-small">HÔTEL</span>
        <span class="brand-large">VALMIRENZA</span>
      </div>
      <p class="room-key-label">Room Key</p>
    </section>

    <div class="side-divider"></div>

    <section class="card-side card-back">
      <div class="tree-backdrop" role="img" aria-label="Bare winter trees silhouetted in light green on a mint background"></div>
      <div class="back-brand">
        <span class="brand-small">HÔTEL</span>
        <span class="brand-large">VALMIRENZA</span>
      </div>
      <p class="contact-line contact-web">www.valmirenza.ch</p>
      <p class="contact-line contact-mail">info@valmirenza.ch</p>
    </section>
  </main>
</body>
</html>
```